Legal Service Estimated Retainer and Average Case Value

We need an 11x14 flyer that contains the standard retainers and average cost be case, both provided in documents, for each case type we handle. We need the information displayed, preferably in a way that makes the information readable but less troubling to a client shocked at price of litigation. We need one sheet with the retainers and average case value merged into one table.

Target Market(s)

Potential Clients

Font styles to use
Serif
Sans Serif

```html
<!DOCTYPE html>
<html lang="en">
<head>
<meta charset="utf-8">
<title>Retainers and Average Fees Flyer</title>
<link href="https://fonts.googleapis.com/css2?family=Arimo:wght@400;700&family=Libre+Caslon+Text:wght@400&display=swap" rel="stylesheet">
<style>
  :root {
    --backdrop: #898989;
    --paper: #ffffff;
    --navy: #0b1a3a;
    --navy-deep: #070f22;
    --navy-mid: #132d4f;
    --panel: #e4e4e6;
    --ink: #1e1e24;
    --white: #ffffff;
  }
  html, body {
    margin: 0;
    padding: 0;
    width: 1200px;
    height: 848px;
    overflow: hidden;
    background: var(--backdrop);
  }
  .flyer {
    position: absolute;
    left: 345px;
    top: 99px;
    width: 510px;
    height: 649px;
    background: var(--paper);
    overflow: hidden;
    font-family: "Arimo", Arial, sans-serif;
  }
  .flyer-art {
    position: absolute;
    inset: 0;
    width: 510px;
    height: 649px;
  }
  .brand {
    position: absolute;
    left: 25px;
    top: 29px;
    display: flex;
    align-items: center;
    gap: 10px;
    color: var(--navy);
    font-family: "Libre Caslon Text", Georgia, serif;
    font-weight: 400;
  }
  .brand-mark {
    width: 30px;
    height: 30px;
    background: var(--navy);
  }
  .brand-name {
    line-height: 1;
  }
  .brand-kicker {
    display: block;
    font-size: 7.5px;
    letter-spacing: 0.3px;
  }
  .brand-title {
    display: block;
    font-size: 15.5px;
    letter-spacing: 0.2px;
    margin-top: 1px;
  }
  .retainers {
    position: absolute;
    left: 13px;
    top: 396px;
    width: 232px;
    color: var(--white);
  }
  .retainers-title {
    margin: 0;
    height: 29px;
    border: 1px solid var(--white);
    border-radius: 15px;
    box-sizing: border-box;
    font-size: 11.2px;
    font-weight: 700;
    line-height: 27px;
    text-align: center;
    letter-spacing: 0.1px;
  }
  .fee-list {
    list-style: none;
    margin: 0;
    padding: 0;
  }
  .retainers .fee-list {
    margin-top: 16px;
    padding: 0 10px 0 7px;
  }
  .fee-row {
    display: flex;
    justify-content: space-between;
    white-space: nowrap;
    font-size: 6.4px;
  }
  .retainers .fee-row {
    height: 13.55px;
    line-height: 13.55px;
  }
  .pfa-note {
    position: absolute;
    left: 13px;
    top: 603px;
    width: 232px;
    height: 30px;
    border-radius: 15px;
    background: var(--navy);
    color: var(--white);
    font-size: 8px;
    font-weight: 700;
    line-height: 30px;
    text-align: center;
    margin: 0;
  }
  .averages {
    position: absolute;
    left: 254px;
    top: 384px;
    width: 244px;
    color: var(--ink);
  }
  .averages-title {
    margin: 0;
    font-size: 11.4px;
    font-weight: 700;
    color: var(--navy);
    text-align: center;
    letter-spacing: 0.1px;
  }
  .averages-intro {
    margin: 6px 10px 0 13px;
    font-size: 6.5px;
    line-height: 8.4px;
  }
  .averages .fee-list {
    margin: 10px 0 0 14px;
  }
  .averages .fee-row {
    justify-content: flex-start;
    height: 11px;
    line-height: 11px;
  }
  .averages .fee-type {
    width: 158px;
  }
</style>
</head>
<body>
  <main class="flyer">
    <svg class="flyer-art" viewBox="0 0 510 649" aria-hidden="false">
      <defs>
        <linearGradient id="navyFade" x1="0" y1="0" x2="0" y2="1">
          <stop offset="0" stop-color="#050b1a"/>
          <stop offset="1" stop-color="#13304f"/>
        </linearGradient>
        <linearGradient id="photoTone" x1="0" y1="0" x2="1" y2="0">
          <stop offset="0" stop-color="#8a8272"/>
          <stop offset="0.35" stop-color="#b9b4aa"/>
          <stop offset="0.55" stop-color="#dcdcdc"/>
          <stop offset="0.8" stop-color="#8e95a3"/>
          <stop offset="1" stop-color="#c9c4b4"/>
        </linearGradient>
        <linearGradient id="silverTop" x1="0" y1="0" x2="1" y2="0">
          <stop offset="0" stop-color="#e6e6e6"/>
          <stop offset="0.6" stop-color="#a9a9a9"/>
          <stop offset="1" stop-color="#1a1a1a"/>
        </linearGradient>
        <linearGradient id="silverBottom" x1="0" y1="0" x2="1" y2="0">
          <stop offset="0" stop-color="#2e2e2e"/>
          <stop offset="0.4" stop-color="#d4d4d4"/>
          <stop offset="0.7" stop-color="#8a8a8a"/>
          <stop offset="1" stop-color="#0e0e0e"/>
        </linearGradient>
      </defs>
      <rect class="navy-field" x="0" y="280" width="510" height="369" fill="url(#navyFade)"/>
      <rect class="fee-panel" x="254" y="300" width="243" height="334" fill="#e4e4e6"/>
      <path class="hero-photo" role="img" aria-label="Photo of a lawyer at a desk pointing a pen at a contract, with a gavel, scales and law books"
            d="M0,220 C120,150 300,80 510,75 L510,283 C400,345 250,375 130,365 C80,360 30,355 0,351 Z"
            fill="url(#photoTone)"/>
      <path class="swoosh-top" d="M55,180 C160,115 330,62 510,58 L510,75 C330,82 180,128 55,180 Z" fill="url(#silverTop)"/>
      <path class="swoosh-bottom" d="M0,351 C30,355 80,360 130,365 C250,375 400,345 510,283 L510,300 C420,355 270,392 140,383 C80,379 30,372 0,368 Z" fill="url(#silverBottom)"/>
    </svg>

    <header class="brand">
      <span class="brand-mark"></span>
      <span class="brand-name">
        <span class="brand-kicker">THE LAW OFFICE OF</span>
        <span class="brand-title">HARLOW M BENNETT</span>
      </span>
    </header>

    <section class="retainers">
      <h2 class="retainers-title">Retainers and Total Estimated Costs:</h2>
      <ul class="fee-list">
        <li class="fee-row"><span>Divorce (3301 C): Retainer:</span><span>$2,000</span></li>
        <li class="fee-row"><span>Divorce (3301 D): Retainer:</span><span>$2,500</span></li>
        <li class="fee-row"><span>Divorce and Custody: Retainer:</span><span>$3,500</span></li>
        <li class="fee-row"><span>Divorce and Equitable Distribution: Retainer:</span><span>$3,500</span></li>
        <li class="fee-row"><span>Divorce and Support: Retainer:</span><span>$3,000</span></li>
        <li class="fee-row"><span>Divorce, Custody and Support: Retainer:</span><span>$3,500</span></li>
        <li class="fee-row"><span>Divorce, Equitable Distribution and Support: Retainer</span><span>$5,000</span></li>
        <li class="fee-row"><span>Divorce, Equitable Distribution, Custody and Support: Retainer:</span><span>$3,500</span></li>
        <li class="fee-row"><span>Custody Initial Order: Retainer</span><span>$3,000</span></li>
        <li class="fee-row"><span>Custody Modification: Retainer:</span><span>$3,500</span></li>
        <li class="fee-row"><span>Custoday and Support: Retainer:</span><span>$3,500</span></li>
      </ul>
    </section>

    <p class="pfa-note">(PFA) Protection From Abuse: $2,000 Paid In Full</p>

    <section class="averages">
      <h2 class="averages-title">Average Fee Per Case Type</h2>
      <p class="averages-intro">In order for our clients to set expectation for legal fees, we provide the national average range of fees per case type. These are only to provide you with an understanding of what other cases have cost clients in similar cases. Please note these are not estimates nor guarantees of your own legal costs.</p>
      <ul class="fee-list">
        <li class="fee-row"><span class="fee-type">Custody Contempt/Modification</span><span>$5,000 - $8,000</span></li>
        <li class="fee-row"><span class="fee-type">Custody Initial Order</span><span>$4,000 - $7,000</span></li>
        <li class="fee-row"><span class="fee-type">Custody &amp; Support</span><span>$5,000 - $8,000</span></li>
        <li class="fee-row"><span class="fee-type">Support</span><span>$2,000 - $4,000</span></li>
        <li class="fee-row"><span class="fee-type">Divorce (3301c)</span><span>$1,500 - $3,000</span></li>
        <li class="fee-row"><span class="fee-type">Divorce (3301d)</span><span>$2,000 - $3,000</span></li>
        <li class="fee-row"><span class="fee-type">Protection and Abuse</span><span>$1,500 - $3,000</span></li>
        <li class="fee-row"><span class="fee-type">Divorce &amp; Custody</span><span>$5,000 - $8,000</span></li>
        <li class="fee-row"><span class="fee-type">Divorce, Equitable Distribution</span><span>$6,000 - $10,000</span></li>
        <li class="fee-row"><span class="fee-type">Divorce, Custory &amp; Support</span><span>$8,000 - $12,000</span></li>
        <li class="fee-row"><span class="fee-type">Divorce, Equitable Distribution &amp; Custody</span><span>$10,000 - $15,000</span></li>
        <li class="fee-row"><span class="fee-type">Divorce, Equitable Distribution &amp; Support</span><span>$8,000 - $12,000</span></li>
        <li class="fee-row"><span class="fee-type">Divorce, Equitable Distribution, Custody &amp; Support</span><span>$12,000 - $15,000</span></li>
      </ul>
    </section>
  </main>
</body>
</html>
```